Etiketten für Rotwein
Zielgruppe
Wir starten dieses Jahr mit unserem ersten Rotwein unserer neuen Marke CAL VERDUNES aus unserem neuen Weingut auf Mallorca.
Es folgen in den kommenden Jahren ein Rosé und weitere Weißweine.
Aufgabenstellung
Wir suchen ein Design für unser erstes Flaschenetikett der Rotweinflaschen.
Die Höhe soll maximal 130 mm sein.
Der Name soll 'Bertoldo' sein.
Die Rebsorte 'Cabernet Sauvignon' und der Jahrgang '2025' sollen mit erscheinen.
Unser Logo sollte mit integriert werden.
Das Erscheinungsbild soll edel, elegant, markant, präsent, wieder erkennbar und einzigartig sein.
Es gibt ein paar Ideen, diese sind aber nur als Hinweise zu verstehen, die verwendet werden könnten.
Dies sind 2 Teddybären im Weinfeld, Teddybären auf einem Traktor im Weinfeld/ Weinberg, Landschaft oder eben komplett etwas anderes Kreatives.
Die Anlagen sind unser Logo in 3 Varianten und einige Beispiele von eigenen unprofessionellen Versuchen, sowie tolle Etikettendesigns die uns gefallen.
We are looking for a design for our first red wine bottle label.
The maximum height should be 130mm.
The name should be 'Bertoldo'.
The grape variety 'Cabernet Sauvignon' and the vintage 2025 should also be included.
Our logo should be integrated.
The overall look should be sophisticated, elegant, striking, memorable, recognizable, and unique.
We have a few ideas, but these are just suggestions that could be used.
These include two teddy bears in a vineyard, teddy bears on a tractor in a vineyard, a landscape, or something completely different and creative.
Attached are our logo in three variations, some examples of our own unprofessional attempts, and some great label designs that we like.
Jens & Uwe
Cal Verdunes

```html
<!DOCTYPE html>
<html lang="de">
<head>
<meta charset="utf-8">
<title>Cal Verdunes – Bertoldo Cabernet Sauvignon 2025</title>
<link rel="stylesheet" href="https://fonts.googleapis.com/css2?family=Montserrat:wght@500;600&family=Pinyon+Script&display=swap">
<style>
  :root {
    --page: #ffffff;
    --label-light: #37415a;
    --label-dark: #1d2334;
    --ink-light: #e6e8ee;
    --ink-soft: #c9ccd6;
    --gold: #c9a053;
    --gold-deep: #a9823c;
  }
  html, body {
    margin: 0;
    padding: 0;
    width: 1200px;
    height: 831px;
    overflow: hidden;
    background: var(--page);
  }
  .canvas {
    position: relative;
    width: 1200px;
    height: 831px;
    display: flex;
    align-items: center;
    justify-content: center;
  }
  .wine-label {
    position: relative;
    width: 500px;
    height: 700px;
    background: radial-gradient(ellipse at 45% 40%, var(--label-light) 0%, #2a3247 55%, var(--label-dark) 100%);
    color: var(--ink-light);
    font-family: "Montserrat", sans-serif;
    text-align: center;
    box-shadow: 0 2px 10px rgba(20, 25, 40, 0.18);
  }
  .brand-name {
    position: absolute;
    top: 50px;
    left: 0;
    right: 0;
    margin: 0;
    font-size: 31px;
    font-weight: 600;
    letter-spacing: 0.5px;
  }
  .brand-region {
    position: absolute;
    top: 94px;
    left: 0;
    right: 0;
    margin: 0;
    font-size: 19px;
    font-weight: 500;
    letter-spacing: 1.5px;
    color: var(--ink-soft);
  }
  .wine-name {
    position: absolute;
    top: 150px;
    left: 0;
    right: 0;
    margin: 0;
    font-family: "Pinyon Script", cursive;
    font-weight: 400;
    font-size: 62px;
    line-height: 1;
    color: var(--gold);
  }
  .estate-mark {
    position: absolute;
    top: 270px;
    left: 50%;
    width: 164px;
    height: 164px;
    margin-left: -82px;
  }
  .estate-mark svg {
    display: block;
  }
  .estate-mark-name {
    position: absolute;
    inset: 0;
    display: flex;
    align-items: center;
    justify-content: center;
    font-size: 13px;
    font-weight: 600;
    letter-spacing: 1.2px;
    color: var(--gold);
  }
  .grape-variety {
    position: absolute;
    top: 525px;
    left: 0;
    right: 0;
    margin: 0;
    font-size: 25px;
    font-weight: 600;
    letter-spacing: 1.5px;
  }
  .edition-number {
    position: absolute;
    top: 562px;
    left: 0;
    right: 0;
    margin: 0;
    font-size: 22px;
    font-weight: 500;
  }
  .vintage-line {
    position: absolute;
    top: 598px;
    left: 0;
    right: 0;
    margin: 0;
    font-size: 15px;
    font-weight: 600;
    letter-spacing: 1.5px;
    color: var(--ink-soft);
  }
</style>
</head>
<body>
  <main class="canvas">
    <article class="wine-label">
      <h1 class="brand-name">CAL VERDUNES</h1>
      <p class="brand-region">MALLORCA</p>
      <p class="wine-name">Bertoldo</p>
      <div class="estate-mark">
        <svg width="164" height="164" viewBox="0 0 164 164" aria-hidden="true">
          <circle cx="82" cy="82" r="78" fill="none" stroke="var(--gold)" stroke-width="3"/>
        </svg>
        <span class="estate-mark-name">CAL VERDUNES</span>
      </div>
      <p class="grape-variety">CABERNET SAUVIGNON</p>
      <p class="edition-number">№ 1</p>
      <p class="vintage-line">SOL DE MALLORCA 2025</p>
    </article>
  </main>
</body>
</html>
```